Stationery Design Project

We are interested in A4 paper letterheads, envelopes, maybe A4 folders where we can put the patients' results in and businesscards. No information will be given out for the time being.
We would like to see mainly shades of white.. please refer to
http://ref.palettorium.net/swatch/Pale_tones_list
anti-flash white, splashed white,ghost white, ivory, snow and white smoke or even light grey
we are interested mainly on the silver design but we welcome the other colors as well. Since its about a gynecologist please avoid dark colors, instead use shades of beige, light grey and white

```html
<!DOCTYPE html>
<html lang="en">
<head>
<meta charset="utf-8">
<title>Harwood Stationery Set</title>
<link href="https://fonts.googleapis.com/css2?family=Abel&display=swap" rel="stylesheet">
<style>
  :root {
    --canvas: #ffffff;
    --folder-face: #ebebeb;
    --folder-flap: #b1b2b4;
    --sheet: #ffffff;
    --sheet-edge: #e4e4e4;
    --decor: #f1f1f1;
    --decor-folder: #f3f3f3;
    --ink: #5a5a5a;
    --mark: #8a8a8a;
  }
  * { margin: 0; padding: 0; box-sizing: border-box; }
  html, body { width: 1200px; height: 1200px; overflow: hidden; background: var(--canvas); }
  body { position: relative; font-family: "Abel", "Arial Narrow", sans-serif; color: var(--ink); }

  .folder { position: absolute; left: 70px; top: 100px; width: 508px; height: 762px; }
  .folder-flap { position: absolute; left: 0; top: 0; width: 508px; height: 50px; }
  .folder-face { position: absolute; left: 0; top: 46px; width: 508px; height: 716px; background: var(--folder-face); overflow: hidden; }

  .letterhead { position: absolute; left: 622px; top: 152px; width: 498px; height: 702px; background: var(--sheet); box-shadow: 0 0 4px var(--sheet-edge); overflow: hidden; }
  .envelope { position: absolute; left: 620px; top: 868px; width: 496px; height: 234px; background: var(--sheet); box-shadow: 0 0 4px var(--sheet-edge); overflow: hidden; }

  .decor-circle { position: absolute; border-radius: 50%; background: var(--decor); }
  .folder-face .decor-circle { background: var(--decor-folder); }

  .contact-block { position: absolute; text-align: right; line-height: 1.2; }
  .contact-block .brand-name { display: block; color: var(--mark); margin-bottom: 14px; }
  .contact-block .practitioner { display: block; margin-bottom: 6px; }
  .contact-block .phone { display: block; margin-top: 6px; }

  .folder-face .contact-block { right: 54px; top: 26px; font-size: 13px; }
  .letterhead .contact-block { right: 42px; top: 20px; font-size: 13px; }
  .envelope .contact-block { right: 24px; bottom: 20px; font-size: 8px; }
  .envelope .contact-block .practitioner { margin-bottom: 3px; }
  .envelope .contact-block .phone { margin-top: 3px; }
</style>
</head>
<body>

  <section class="folder" aria-label="Presentation folder">
    <svg class="folder-flap" viewBox="0 0 508 50" aria-hidden="true">
      <polygon points="0,46 456,0 456,4 508,46" fill="var(--folder-flap)"/>
    </svg>
    <div class="folder-face">
      <div class="decor-circle" style="left:150px; top:300px; width:300px; height:300px;"></div>
      <address class="contact-block">
        <span class="brand-name">Harwood</span>
        <span class="practitioner">Dr. L Harwood (B. Med)</span>
        Suite 4, 212 Ellery Road<br>
        SYDNEY NSW 2000
        <span class="phone">02 9000 4127</span>
      </address>
    </div>
  </section>

  <section class="letterhead" aria-label="A4 letterhead">
    <div class="decor-circle" style="left:20px; top:370px; width:260px; height:260px;"></div>
    <address class="contact-block">
      <span class="brand-name">Harwood</span>
      <span class="practitioner">Dr. L Harwood (B. Med)</span>
      Suite 4, 212 Ellery Road<br>
      SYDNEY NSW 2000
      <span class="phone">02 9000 4127</span>
    </address>
  </section>

  <section class="envelope" aria-label="DL envelope">
    <div class="decor-circle" style="left:14px; top:40px; width:150px; height:150px;"></div>
    <address class="contact-block">
      <span class="practitioner">Dr. L Harwood (B. Med)</span>
      Suite 4, 212 Ellery Road<br>
      SYDNEY NSW 2000
      <span class="phone">02 9000 4127</span>
    </address>
  </section>

</body>
</html>
```